Corporate consulting business needs a business card

I want a professional business card.... surprise me

Updates

Reason: i dont think 2 days is enough

Target Market(s)

Corprorate and Not for Profit firms and organisations

Industry/Entity Type

Consulting

Contact Information for Business Card

Logo
Corporate Consulting Services
On Time, On Budget, Beyond Expectation
Tovan Presfield
Director
0427 31 94 62 (Larger)
tovan@tp-advisory.com.au
www.tp-advisory.com.au
include little icons beside the contact info:

- Envelope = email
- Phone = phone
- Globe = website

Font styles to use
Serif
Sans Serif

Requirements
Must have
• Professional and clean
Nice to have
• you tell me

```html
<!DOCTYPE html>
<html lang="en">
<head>
<meta charset="utf-8">
<title>TP Advisory – Business Card</title>
<link rel="stylesheet" href="https://fonts.googleapis.com/css2?family=Libre+Baskerville&family=Comfortaa:wght@700&family=Questrial&display=swap">
<style>
  :root {
    --brown: #4a2511;
    --ink-grey: #8a8a8a;
    --rule-grey: #b5b5b5;
    --paper: #ffffff;
    --backdrop: #ececec;
    --band-text: #ffffff;
  }
  * { box-sizing: border-box; margin: 0; padding: 0; }
  html, body { width: 1138px; height: 1200px; overflow: hidden; }
  body { background: var(--backdrop); position: relative; font-family: "Questrial", sans-serif; }

  .card {
    position: absolute;
    left: 119px;
    width: 900px;
    height: 514px;
    background: var(--paper);
    box-shadow: 0 4px 14px rgba(0,0,0,0.12);
  }
  .card--front { top: 60px; }
  .card--back { top: 626px; }

  /* Front */
  .brand {
    position: absolute;
    left: 0; right: 0; top: 110px;
    display: flex; flex-direction: column; align-items: center;
    color: var(--brown);
    font-family: "Libre Baskerville", serif;
  }
  .brand__mark {
    width: 96px; height: 96px;
    border: 4px solid var(--brown);
    border-radius: 50%;
    margin-bottom: 18px;
  }
  .brand__name { font-size: 34px; letter-spacing: 1px; line-height: 1; }
  .brand__services { font-size: 21px; letter-spacing: 1px; text-transform: uppercase; margin-top: 12px; }

  .tagline-band {
    position: absolute;
    left: 0; right: 0; top: 372px; height: 36px;
    background: var(--brown);
    color: var(--band-text);
    font-size: 15px; letter-spacing: 1px; text-transform: uppercase;
    display: flex; align-items: center; justify-content: flex-end;
    padding-right: 70px;
  }

  /* Back */
  .back-brand {
    position: absolute;
    left: 60px; top: 178px; width: 240px;
    display: flex; flex-direction: column; align-items: center;
    color: var(--brown);
    font-family: "Libre Baskerville", serif;
  }
  .back-brand__mark {
    width: 110px; height: 110px;
    border: 4px solid var(--brown);
    border-radius: 50%;
    margin-bottom: 14px;
  }
  .back-brand__name { font-size: 22px; letter-spacing: 1px; }

  .divider {
    position: absolute;
    left: 330px; top: 150px; width: 1px; height: 200px;
    background: var(--rule-grey);
  }

  .contact { position: absolute; left: 356px; top: 140px; }
  .contact__name {
    font-family: "Comfortaa", sans-serif; font-weight: 700;
    font-size: 38px; color: var(--brown);
    text-transform: uppercase; letter-spacing: 1px; line-height: 1;
  }
  .contact__role { font-size: 16px; color: var(--ink-grey); margin-top: 6px; }
  .contact__list { list-style: none; margin-top: 26px; }
  .contact__item {
    display: flex; align-items: center;
    font-size: 24px; color: var(--ink-grey); line-height: 1.35;
  }
  .contact__item--phone { color: var(--brown); font-size: 27px; }
  .contact__icon { width: 18px; height: 18px; margin-right: 16px; flex: none; }
  .contact__icon * { fill: var(--brown); }
  .contact__icon .stroke { fill: none; stroke: var(--brown); stroke-width: 1.8; }
</style>
</head>
<body>

<section class="card card--front">
  <div class="brand">
    <div class="brand__mark"></div>
    <div class="brand__name">TP Advisory</div>
    <div class="brand__services">Consulting Services</div>
  </div>
  <div class="tagline-band">On Time | On Budget | Beyond Expectation</div>
</section>

<section class="card card--back">
  <div class="back-brand">
    <div class="back-brand__mark"></div>
    <div class="back-brand__name">TP Advisory</div>
  </div>

  <div class="divider"></div>

  <div class="contact">
    <div class="contact__name">Tovan Presfield</div>
    <div class="contact__role">Director</div>
    <ul class="contact__list">
      <li class="contact__item contact__item--phone">
        <svg class="contact__icon" viewBox="0 0 24 24" aria-hidden="true">
          <path d="M6.6 10.8a15.1 15.1 0 0 0 6.6 6.6l2.2-2.2c.3-.3.7-.4 1-.2 1.1.4 2.3.6 3.6.6.6 0 1 .4 1 1V20c0 .6-.4 1-1 1C10.6 21 3 13.4 3 4c0-.6.4-1 1-1h3.5c.6 0 1 .4 1 1 0 1.3.2 2.5.6 3.6.1.3 0 .7-.2 1z"/>
        </svg>
        0427 31 94 62
      </li>
      <li class="contact__item">
        <svg class="contact__icon" viewBox="0 0 24 24" aria-hidden="true">
          <path d="M2 5h20v14H2z"/>
          <path d="M2 5l10 8 10-8" style="fill:none;stroke:#fff;stroke-width:1.8"/>
        </svg>
        tovan@tp-advisory.com.au
      </li>
      <li class="contact__item">
        <svg class="contact__icon" viewBox="0 0 24 24" aria-hidden="true">
          <circle class="stroke" cx="12" cy="12" r="9.5"/>
          <ellipse class="stroke" cx="12" cy="12" rx="4" ry="9.5"/>
          <path class="stroke" d="M2.5 12h19M4 7h16M4 17h16"/>
        </svg>
        www.tp-advisory.com.au
      </li>
    </ul>
  </div>
</section>

</body>
</html>
```